Business Card Design Project

Please create a custom business card for 'Journeys beyond the lantern'. The logo is attached to this brief.

Here is the link to the logo project : http://tasks.pixelmarrow.net/task.aspx?id=392017

Questions can be posted on the Discussion Board.

```html
<!DOCTYPE html>
<html lang="en">
<head>
<meta charset="utf-8">
<title>Lanternway Business Card</title>
<link href="https://fonts.googleapis.com/css2?family=Open+Sans:wght@300;400;600&display=swap" rel="stylesheet">
<style>
  :root {
    --page-bg: #e9e6e1;
    --card-white: #ffffff;
    --card-grey: #f1f1f1;
    --brand-red: #e0262b;
    --brand-red-dark: #c81d22;
    --ink: #2b2b2b;
    --ink-soft: #555555;
    --on-red: #ffffff;
  }
  * { margin: 0; padding: 0; box-sizing: border-box; }
  html, body {
    width: 1200px;
    height: 1023px;
    overflow: hidden;
    background: var(--page-bg);
    font-family: "Open Sans", Arial, sans-serif;
  }
  .canvas {
    position: relative;
    width: 1200px;
    height: 1023px;
  }
  .card {
    position: absolute;
    left: 100px;
    top: 222px;
    width: 1000px;
    height: 580px;
    border-radius: 22px;
    overflow: hidden;
    background: linear-gradient(180deg, var(--card-white) 0%, var(--card-grey) 100%);
    box-shadow: 0 14px 40px rgba(0,0,0,0.18);
  }
  .card-band {
    position: absolute;
    left: 0;
    right: 0;
    top: 318px;
    bottom: 0;
    background: linear-gradient(180deg, var(--brand-red) 0%, var(--brand-red-dark) 100%);
  }
  .holder {
    position: absolute;
    right: 60px;
    top: 44px;
    text-align: right;
    color: var(--ink);
  }
  .holder-name {
    font-size: 46px;
    font-weight: 400;
    line-height: 1.1;
  }
  .holder-role {
    font-size: 26px;
    font-weight: 300;
    color: var(--ink-soft);
  }
  .brand {
    position: absolute;
    left: 58px;
    top: 178px;
    display: flex;
    align-items: center;
    gap: 26px;
  }
  .brand-mark {
    width: 112px;
    height: 112px;
    background: var(--brand-red);
    border-radius: 10px;
  }
  .brand-name {
    font-size: 118px;
    font-weight: 400;
    color: var(--brand-red);
    line-height: 1;
    letter-spacing: 1px;
  }
  .contacts {
    position: absolute;
    left: 60px;
    top: 352px;
    list-style: none;
    color: var(--on-red);
    font-size: 22px;
    font-weight: 300;
  }
  .contacts li {
    display: flex;
    align-items: center;
    gap: 14px;
    height: 44px;
  }
  .contacts svg {
    width: 22px;
    height: 22px;
    flex: none;
  }
  .address {
    position: absolute;
    right: 60px;
    top: 360px;
    text-align: right;
    color: var(--on-red);
    font-size: 28px;
    font-weight: 300;
    line-height: 1.35;
  }
</style>
</head>
<body>
<main class="canvas">
  <section class="card" aria-label="Business card front">
    <div class="card-band"></div>

    <header class="holder">
      <p class="holder-name">Your Name</p>
      <p class="holder-role">Designation</p>
    </header>

    <div class="brand">
      <div class="brand-mark"></div>
      <span class="brand-name">Lanternway</span>
    </div>

    <ul class="contacts">
      <li>
        <svg viewBox="0 0 24 24" aria-hidden="true"><path fill="#fff" d="M6.6 10.8a15.1 15.1 0 0 0 6.6 6.6l2.2-2.2c.3-.3.7-.4 1-.2 1.1.4 2.3.6 3.6.6.6 0 1 .4 1 1V20c0 .6-.4 1-1 1A17 17 0 0 1 3 4c0-.6.4-1 1-1h3.5c.6 0 1 .4 1 1 0 1.3.2 2.5.6 3.6.1.3 0 .7-.2 1z"/></svg>
        <span>0123 456 789</span>
      </li>
      <li>
        <svg viewBox="0 0 24 24" aria-hidden="true"><rect x="4" y="4" width="16" height="16" fill="none" stroke="#fff" stroke-width="2"/></svg>
        <span>0123 456 789</span>
      </li>
      <li>
        <svg viewBox="0 0 24 24" aria-hidden="true"><rect x="3" y="6" width="18" height="12" fill="none" stroke="#fff" stroke-width="2"/><path d="M3 6l9 7 9-7" fill="none" stroke="#fff" stroke-width="2"/></svg>
        <span>youremail@mailpost.com</span>
      </li>
      <li>
        <svg viewBox="0 0 24 24" aria-hidden="true"><circle cx="12" cy="12" r="9" fill="none" stroke="#fff" stroke-width="2"/><path d="M3 12h18M12 3c3 3 3 15 0 18M12 3c-3 3-3 15 0 18" fill="none" stroke="#fff" stroke-width="1.5"/></svg>
        <span>www.yourwebsite.com</span>
      </li>
    </ul>

    <address class="address">
      Your address can put here<br>
      Your address can put here<br>
      Your address can put here
    </address>
  </section>
</main>
</body>
</html>
```